Price Calculator as Responsive Web App to support Sales People

We need to build a simple micro web app to support sales people in making quotes. We already have a backend that can take a number of parameters and create a quote. We need put a responsive web app on top of this so that our people on the road can easily do their price simulations.

We need two pages. One for the input and another for the results. No menus, navigations, etc. It is 6 different inputs as shown with boxes in the sketch. They don't need to be boxed, but some of them have a bit of instruction text that clearly need to belong to the input.

This needs to be responsive, but first and foremost designed for smartphones. I have included a background gradient that we would like to use -- or a variant of it. We expect this to be delivered as HTML/CSS + images so that we can quickly write a few pieces of JavaScript ourselves to wire it up to our price simulator.

Industry/Entity Type

Information Technology

Coding

Coded - Design and coding required

Number of Pages Required

2 page

Font styles to use
Sans Serif

Requirements
Must have
• Responsive design
• Easy to wire up JavaScript to the HTML/CSS
Nice to have
• Some quick way to pick number of months. +/- buttons to add remove a year or 3 months. Same thing with number of items. Add 10 or 5 quickly.
• Maybe some parallax effect while scrolling as long as it is not distracting.
Should not have
• Toolbars, Menus, Navigations, Banners, etc. This is just a single micro app.

```html
<!DOCTYPE html>
<html lang="en">
<head>
<meta charset="utf-8">
<title>Price Calculator</title>
<link href="https://fonts.googleapis.com/css2?family=Montserrat:wght@400;500;700;800&display=swap" rel="stylesheet">
<style>
:root{
  --page:#2b2d3a;
  --panel:#0099ff;
  --tile:#0a8ded;
  --tile-text:#0b6fc7;
  --rule:#0a4f8f;
  --white:#ffffff;
  --ink:#111214;
  --orange:#ff6a00;
  --green-a:#00c241;
  --green-b:#00aa46;
  --red-a:#ff1a00;
  --red-b:#dd1200;
  --knob:#0a7fd9;
  --knob-ring:#0567b8;
  --grid:#1a84da;
  --line:#4fc6b8;
  --axis-text:#a8561e;
}
*{box-sizing:border-box;margin:0;padding:0}
html,body{width:1200px;height:1200px;overflow:hidden}
body{background:var(--page);font-family:"Montserrat",sans-serif;color:var(--white);position:relative}
.panel{position:absolute;background:var(--panel);overflow:hidden}
.input-panel{left:330px;top:12px;width:541px;height:570px}
.results-panel{left:332px;top:609px;width:536px;height:565px}
.abs{position:absolute}
.field-title{font-weight:800;font-size:12.5px}
.label{font-size:10px;font-weight:500}
.rule{position:absolute;left:0;right:0;height:1px;background:var(--rule)}
.track{position:absolute;height:1px;background:var(--rule)}
.knob{position:absolute;width:26px;height:26px;border-radius:50%;border:6px solid var(--knob-ring);background:var(--knob);transform:translate(-50%,-50%)}
.tick{position:absolute;font-size:5px;color:#1f8fe6;transform:translateX(-50%)}
.big-value{font-weight:800;font-size:26px;transform:translateY(-50%)}
.unit{font-size:10px;transform:translateY(-50%)}
.tile{position:absolute;background:var(--tile);color:var(--tile-text);border-radius:2px;display:flex;flex-direction:column;align-items:center;justify-content:center;text-align:center;font-size:9px;line-height:1.35}
.tile b{font-weight:700}
.tile.small{font-weight:700;font-size:9px}
.tile.active{background:var(--ink);color:var(--white)}
.info{position:absolute;display:flex;gap:7px;align-items:center;font-size:7px;color:#0b5da8;line-height:1.45}
.info i{flex:0 0 10px;height:10px;border-radius:50%;background:#2aa4ff;font-style:normal;font-size:6px;color:#7fc8ff;display:flex;align-items:center;justify-content:center}
.select{position:absolute;height:24px;background:var(--white);color:#333;font-size:9px;display:flex;align-items:center;justify-content:space-between;padding:0 6px 0 11px;border:1px solid #d0d0d0}
.select span:last-child{font-size:6px;color:#222}
.vrule{position:absolute;width:1px;background:var(--rule)}
.btn-quote{position:absolute;background:var(--orange);color:var(--white);font-weight:800;font-size:9.5px;display:flex;align-items:center;justify-content:center}
.tab{position:absolute;display:flex;align-items:center;justify-content:center;font-weight:700;font-size:9px;border-radius:2px}
.card{position:absolute;padding:14px 12px}
.card .num{font-weight:800;font-size:38px;line-height:1;letter-spacing:-0.5px}
.card .cap{font-size:10px;margin-top:9px}
.card.total{background:linear-gradient(180deg,var(--green-a),var(--green-b))}
.card.cap-card{background:linear-gradient(180deg,var(--red-a),var(--red-b))}
.row-label{position:absolute;left:18px;font-size:10px;transform:translateY(-50%)}
.row-value{position:absolute;left:274px;font-weight:800;font-size:12px;transform:translateY(-50%)}
.chart{position:absolute;left:0;top:0}
.review{position:absolute;font-weight:800;font-size:9.5px;color:var(--ink);transform:translate(-50%,-50%)}
.dot{position:absolute;top:1179px;width:9px;height:9px;border-radius:50%}
</style>
</head>
<body>

<section class="panel input-panel">
  <div class="abs field-title" style="left:16px;top:26px">Duration</div>
  <div class="track" style="left:97px;width:321px;top:34px"></div>
  <div class="knob" style="left:97px;top:34px"></div>
  <div class="knob" style="left:161px;top:34px"></div>
  <div class="knob" style="left:226px;top:34px"></div>
  <div class="knob" style="left:290px;top:34px"></div>
  <div class="knob" style="left:354px;top:34px"></div>
  <div class="knob" style="left:418px;top:34px"></div>
  <div class="tick" style="left:97px;top:63px">1 MO</div>
  <div class="tick" style="left:161px;top:63px">6 MO</div>
  <div class="tick" style="left:226px;top:63px">9 MO</div>
  <div class="tick" style="left:290px;top:63px">12 MO</div>
  <div class="tick" style="left:354px;top:63px">18 MO</div>
  <div class="tick" style="left:418px;top:63px">24 MO</div>
  <div class="abs big-value" style="left:444px;top:34px">12</div>
  <div class="abs unit" style="left:485px;top:34px">Months</div>

  <div class="abs field-title" style="left:21px;top:88px">Count</div>
  <div class="track" style="left:93px;width:335px;top:94px"></div>
  <div class="knob" style="left:93px;top:94px"></div>
  <div class="abs big-value" style="left:450px;top:94px">6</div>
  <div class="abs unit" style="left:489px;top:94px">Items</div>

  <div class="rule" style="top:135px"></div>

  <div class="abs label" style="left:13px;top:158px">Engine Power (Beyond Standard)</div>
  <div class="tile" style="left:15px;top:183px;width:124px;height:52px"><b>$360 per year</b><span>(Bronze Power)</span></div>
  <div class="tile" style="left:144px;top:183px;width:124px;height:52px"><b>$600 per year</b><span>(Silver Power)</span></div>
  <div class="tile" style="left:273px;top:183px;width:124px;height:52px"><b>$1M per year</b><span>(Gold Power)</span></div>
  <div class="tile" style="left:402px;top:183px;width:124px;height:52px"><b>$3M per year</b><span>(Platinum Power)</span></div>
  <div class="info" style="left:23px;top:245px"><i>i</i><span>A basic engine Lorem ipsum dolor sit amet, consectetur adipiscing elit. Suspendisse varius enim in eros elementum tristique.</span></div>

  <div class="rule" style="top:262px"></div>

  <div class="abs label" style="left:13px;top:285px">Shared Storage Addition</div>
  <div class="tile small" style="left:18px;top:310px;width:93px;height:40px">10 KG</div>
  <div class="tile small active" style="left:121px;top:310px;width:93px;height:40px">50 KG</div>
  <div class="tile small" style="left:224px;top:310px;width:93px;height:40px">100 KG</div>
  <div class="tile small" style="left:327px;top:310px;width:93px;height:40px">500 KG</div>
  <div class="tile small" style="left:430px;top:310px;width:94px;height:40px">1 TON</div>
  <div class="info" style="left:23px;top:359px"><i>i</i><span>A basic engine Lorem ipsum dolor sit amet, consectetur adipiscing elit. Suspendisse varius enim in eros elementum tristique.</span></div>

  <div class="rule" style="top:377px"></div>
  <div class="vrule" style="left:270px;top:377px;height:127px"></div>

  <div class="abs label" style="left:14px;top:400px">Additional Tip</div>
  <div class="select" style="left:14px;top:422px;width:243px"><span>Select one...</span><span>▼</span></div>
  <div class="info" style="left:14px;top:464px;width:240px"><i>i</i><span>A basic engine Lorem ipsum dolor sit amet, consectetur adipiscing elit. Suspendisse varius enim in eros elementum tristique.</span></div>

  <div class="abs label" style="left:284px;top:400px">Elastic Extension</div>
  <div class="select" style="left:284px;top:422px;width:244px"><span>Select one...</span><span>▼</span></div>
  <div class="info" style="left:284px;top:464px;width:240px"><i>i</i><span>A basic engine Lorem ipsum dolor sit amet, consectetur adipiscing elit. Suspendisse varius enim in eros elementum tristique.</span></div>

  <div class="rule" style="top:504px;opacity:.35"></div>
  <div class="btn-quote" style="left:321px;top:526px;width:187px;height:38px">GET QUOTE</div>
</section>

<section class="panel results-panel">
  <div class="abs field-title" style="left:12px;top:18px">Your Results</div>
  <div class="tab" style="left:258px;top:45px;width:128px;height:37px;background:var(--ink);color:var(--white)">PER MONTH</div>
  <div class="tab" style="left:393px;top:45px;width:127px;height:37px;background:var(--tile);color:var(--tile-text)">PER YEAR</div>

  <div class="card total" style="left:19px;top:93px;width:242px;height:91px"><div class="num">852</div><div class="cap">Total</div></div>
  <div class="card cap-card" style="left:274px;top:93px;width:243px;height:91px"><div class="num">1278</div><div class="cap">Cap</div></div>

  <div class="row-label" style="top:207px">Items</div><div class="row-value" style="top:206px">350</div>
  <div class="row-label" style="top:238px">Engine</div><div class="row-value" style="top:237px">250</div>
  <div class="row-label" style="top:269px">Storage</div><div class="row-value" style="top:268px">200</div>
  <div class="row-label" style="top:300px">Tip</div><div class="row-value" style="top:298px">52</div>

  <svg class="chart" width="536" height="565" viewBox="0 0 536 565" role="img" aria-label="Line chart of quote trend">
    <rect x="215" y="340" width="26" height="8" fill="none" stroke="var(--line)" stroke-width="2"/>
    <text x="246" y="347" font-family="Montserrat, sans-serif" font-size="6.5" font-weight="700" fill="var(--axis-text)">My First Dataset</text>
    <g stroke="var(--grid)" stroke-width="1">
      <line x1="30" y1="360" x2="513" y2="360"/><line x1="30" y1="377.5" x2="513" y2="377.5"/>
      <line x1="30" y1="395" x2="513" y2="395"/><line x1="30" y1="412.5" x2="513" y2="412.5"/>
      <line x1="30" y1="430" x2="513" y2="430"/><line x1="30" y1="447.5" x2="513" y2="447.5"/>
      <line x1="30" y1="465" x2="513" y2="465"/><line x1="30" y1="482.5" x2="513" y2="482.5"/>
      <line x1="30" y1="500" x2="513" y2="500"/>
      <line x1="111" y1="360" x2="111" y2="500"/><line x1="191" y1="360" x2="191" y2="500"/>
      <line x1="272" y1="360" x2="272" y2="500"/><line x1="352" y1="360" x2="352" y2="500"/>
      <line x1="433" y1="360" x2="433" y2="500"/><line x1="513" y1="360" x2="513" y2="500"/>
    </g>
    <line x1="30" y1="360" x2="30" y2="500" stroke="#0d6dbd"/>
    <g font-family="Montserrat, sans-serif" font-size="6" fill="var(--axis-text)" text-anchor="end">
      <text x="26" y="362">85</text><text x="26" y="379.5">80</text><text x="26" y="397">75</text>
      <text x="26" y="414.5">70</text><text x="26" y="432">65</text><text x="26" y="449.5">60</text>
      <text x="26" y="467">55</text><text x="26" y="484.5">50</text><text x="26" y="502">45</text>
    </g>
    <path d="M30 430 L111 451 C140 420 165 395 191 377.5 C220 374 250 373 272 373.5 C300 405 325 440 352 461.5 C380 463 410 463 433 464 C460 475 490 487 513 493" fill="none" stroke="var(--line)" stroke-width="2"/>
    <g fill="var(--panel)" stroke="var(--line)" stroke-width="1">
      <circle cx="30" cy="430" r="2"/><circle cx="111" cy="451" r="2"/><circle cx="191" cy="377.5" r="2"/>
      <circle cx="272" cy="373.5" r="2"/><circle cx="352" cy="461.5" r="2"/><circle cx="433" cy="464" r="2"/>
      <circle cx="513" cy="493" r="2"/>
    </g>
  </svg>

  <div class="review" style="left:128px;top:537px">REVIEW</div>
  <div class="btn-quote" style="left:318px;top:518px;width:184px;height:38px">GET QUOTE</div>
</section>

<div class="dot" style="left:587px;background:#c8c8c8"></div>
<div class="dot" style="left:604px;background:#00c241"></div>

</body>
</html>
```